Flyer for the Harvest of lanterns conference

Flyer design for an annual international conference called "MERIVAL 2017". This is a conference for young adults, so we hope to produce a design that is both professional and appealing to young people in general

We'd like the flyer to showcase the conference brand logo, and clearly highlight the key information to people who will read it.

Target Market(s)

Young people, young adults

Industry/Entity Type

Religious

Font styles to use
Sans Serif

Colors

Designer to choose colors to be used in the design.

Requirements
Must have
• - Should be only one page (Vertical or Horizontal).
• - the MERVAL logo and all the information found in the attached text file. This includes: Main topic: Your sons and daughters shall prophesy,
• Dates and time, location, contact information and everything that is in the attached text file.
Nice to have
• It would be nice to see samples where the white logo is used and another where the black one is used.
Should not have
• This is NOT a folded flyer, we will be sticking it on doors and public places. And we will be printing large simple to put on walls. So only one page with few words like an add (the words are in the attached file)

```html
<!DOCTYPE html>
<html lang="en">
<head>
<meta charset="utf-8">
<title>Harvest of Lanterns Conference — MERIVAL 2017</title>
<link rel="stylesheet" href="https://fonts.googleapis.com/css2?family=Montserrat:wght@400;600;700;800&family=Oswald:wght@500;600;700&display=swap">
<style>
  :root {
    --page-bg: #e6e6e6;
    --paper: #f4f4f4;
    --paper-shade: #d8d8d8;
    --ink: #1b1b1b;
    --charcoal: #2b2b2b;
    --maroon: #4a1a16;
    --yellow: #f7d31f;
    --gold: #f4b51a;
    --amber: #f39a12;
    --orange: #e6620f;
    --orange-deep: #d2410f;
    --rust: #8c3810;
    --grey-panel: #c7c7c7;
    --grey-text: #3a3a3a;
    --white: #ffffff;
    --photo-light: #ddd3c4;
    --photo-dark: #7e6e5c;
  }
  html, body {
    margin: 0;
    width: 1200px;
    height: 1200px;
    overflow: hidden;
    background: var(--page-bg);
  }
  .flyer {
    position: absolute;
    left: 197px;
    top: 30px;
    width: 806px;
    height: 1140px;
    box-shadow: 0 6px 24px rgba(0,0,0,.18);
  }
  .display { font-family: 'Oswald', 'Arial Narrow', sans-serif; }
  .body-text { font-family: 'Montserrat', Arial, sans-serif; }
</style>
</head>
<body>
<svg class="flyer" viewBox="258 50 982 1387" xmlns="http://www.w3.org/2000/svg">
  <defs>
    <linearGradient id="paper-fill" x1="0" y1="0" x2="0" y2="1">
      <stop offset="0" stop-color="var(--paper)"/>
      <stop offset="1" stop-color="var(--paper-shade)"/>
    </linearGradient>
    <linearGradient id="sun-fill" x1="0" y1="0" x2="1" y2="1">
      <stop offset="0" stop-color="var(--amber)"/>
      <stop offset="1" stop-color="var(--yellow)"/>
    </linearGradient>
    <linearGradient id="photo-fill" x1="0" y1="0" x2="1" y2="1">
      <stop offset="0" stop-color="var(--photo-light)"/>
      <stop offset="1" stop-color="var(--photo-dark)"/>
    </linearGradient>
    <linearGradient id="glow-fill" x1="0" y1="0" x2="0" y2="1">
      <stop offset="0" stop-color="var(--yellow)"/>
      <stop offset="1" stop-color="var(--orange-deep)"/>
    </linearGradient>
    <linearGradient id="skyline-fill" x1="0" y1="0" x2="0" y2="1">
      <stop offset="0" stop-color="var(--rust)" stop-opacity="0"/>
      <stop offset=".45" stop-color="var(--rust)" stop-opacity=".85"/>
      <stop offset="1" stop-color="var(--rust)"/>
    </linearGradient>
    <linearGradient id="footer-fill" x1="0" y1="0" x2="1" y2="1">
      <stop offset="0" stop-color="var(--yellow)"/>
      <stop offset="1" stop-color="var(--gold)"/>
    </linearGradient>
  </defs>

  <!-- base paper -->
  <rect class="paper" x="258" y="50" width="982" height="1387" fill="url(#paper-fill)"/>

  <!-- top-left sunburst shards -->
  <polygon class="shard" points="258,50 780,50 640,380 258,130" fill="url(#sun-fill)"/>
  <polygon class="shard shard--light" points="560,120 700,50 860,560 620,400" fill="var(--yellow)" opacity=".85"/>

  <!-- hero photo area -->
  <polygon class="hero-photo" role="img" aria-label="Photo of a young man in a hooded jacket looking out over a misty city"
           points="720,50 1240,50 1240,190 855,555" fill="url(#photo-fill)"/>

  <!-- dark info band -->
  <polygon class="info-band" points="1240,185 1240,620 780,1052 935,1198 860,1198 520,880" fill="var(--ink)"/>

  <!-- speakers panel -->
  <polygon class="speakers-panel" points="1240,620 1240,1196 930,1196 780,1052" fill="var(--grey-panel)"/>

  <!-- footer glow -->
  <polygon class="footer-glow" points="690,1030 930,1196 1240,1196 1240,1437 690,1437" fill="url(#footer-fill)"/>

  <!-- orange theme block -->
  <polygon class="theme-block" points="258,660 690,1040 690,1437 258,1437" fill="var(--orange)"/>
  <polygon class="theme-edge" points="258,660 290,690 290,1437 258,1437" fill="var(--gold)"/>
  <polygon class="theme-accent" points="290,690 400,855 290,855" fill="var(--orange-deep)"/>
  <rect class="skyline" role="img" aria-label="City skyline silhouette" x="290" y="1190" width="400" height="247" fill="url(#skyline-fill)"/>

  <!-- conference badge -->
  <g class="brand-badge">
    <circle cx="478" cy="272" r="192" fill="var(--charcoal)"/>
    <text class="body-text" x="478" y="320" text-anchor="middle" font-size="62" font-weight="700" fill="var(--white)" letter-spacing="3">MERVAL</text>
  </g>

  <!-- conference title -->
  <g class="conference-title">
    <text class="display" x="615" y="550" text-anchor="end" font-size="64" font-weight="600" fill="var(--maroon)" textLength="275" lengthAdjust="spacingAndGlyphs">HARVEST</text>
    <text class="display" transform="translate(425,615) rotate(-90)" text-anchor="middle" font-size="58" font-weight="700" fill="var(--charcoal)">OF</text>
    <text class="display" x="615" y="662" text-anchor="end" font-size="108" font-weight="600" fill="url(#glow-fill)" textLength="175" lengthAdjust="spacingAndGlyphs">LANTERNS</text>
    <rect x="340" y="672" width="274" height="52" rx="26" fill="var(--charcoal)"/>
    <text class="body-text" x="477" y="712" text-anchor="middle" font-size="36" font-weight="400" fill="var(--gold)">CONFERENCE</text>
  </g>

  <!-- date -->
  <g class="event-date">
    <g class="icon-calendar" fill="none" stroke="var(--white)" stroke-width="2.5">
      <rect x="1173" y="334" width="32" height="26" rx="2"/>
      <line x1="1173" y1="341" x2="1205" y2="341"/>
      <line x1="1181" y1="329" x2="1181" y2="336"/><line x1="1197" y1="329" x2="1197" y2="336"/>
      <path d="M1180 347h4M1187 347h4M1194 347h4M1180 353h4M1187 353h4M1194 353h4"/>
    </g>
    <text class="body-text" x="1208" y="397" text-anchor="end" font-size="30" font-weight="700" fill="var(--gold)">SEPTEMBER</text>
    <polygon points="850,495 960,407 1240,407 1240,497" fill="var(--yellow)"/>
    <text class="body-text" x="1208" y="488" text-anchor="end" font-size="92" font-weight="800" fill="var(--ink)">1<tspan font-size="46" dy="-38">st</tspan><tspan font-size="92" dy="38">–3</tspan><tspan font-size="46" dy="-38">rd</tspan></text>
    <polygon points="958,500 1240,500 1240,580 985,580" fill="var(--ink)"/>
    <text class="display" x="1206" y="568" text-anchor="end" font-size="70" font-weight="600" fill="var(--white)">2017</text>
  </g>

  <!-- start time -->
  <g class="event-time">
    <g class="icon-clock" fill="none" stroke="var(--white)" stroke-width="3">
      <circle cx="886" cy="662" r="16"/><path d="M886 652v10l7 5"/>
    </g>
    <text class="display" x="922" y="677" font-size="38" font-weight="500" fill="var(--gold)">START TIME</text>
    <text class="body-text" x="866" y="735" font-size="46" font-weight="700" fill="var(--white)">6:00PM</text>
  </g>

  <!-- location -->
  <g class="event-location">
    <g class="icon-pin" fill="none" stroke="var(--white)" stroke-width="3">
      <path d="M719 813c-9-12-14-19-14-27a14 14 0 0 1 28 0c0 8-5 15-14 27z"/>
      <circle cx="719" cy="786" r="5"/>
    </g>
    <text class="display" x="746" y="818" font-size="46" font-weight="500" fill="var(--gold)">LOCATION</text>
    <text class="body-text" font-size="19" font-weight="400" fill="var(--white)" text-anchor="middle">
      <tspan x="796" y="842">Lakeside Harbor Inn</tspan>
      <tspan x="796" y="866">418 Cedar Avenue Westbrook,</tspan>
      <tspan x="796" y="889">ME 04092 United States</tspan>
    </text>
  </g>

  <!-- room -->
  <g class="event-room">
    <g class="icon-door" fill="none" stroke="var(--white)" stroke-width="2.5">
      <rect x="682" y="932" width="15" height="28"/><circle cx="693" cy="947" r="1.5" fill="var(--white)"/>
    </g>
    <text class="display" x="710" y="963" font-size="42" font-weight="500" fill="var(--gold)">ROOM</text>
    <text class="body-text" x="660" y="990" font-size="16" font-weight="600" fill="var(--white)">Maple Ballroom</text>
  </g>

  <!-- speakers -->
  <g class="speakers">
    <g class="icon-podium" fill="var(--ink)">
      <path d="M1156 795h42v12h-42z"/>
      <path d="M1162 809h30v30h-30z"/>
    </g>
    <text class="display" x="1205" y="903" text-anchor="end" font-size="56" font-weight="600" fill="var(--grey-text)">SPEAKERS</text>
    <g class="display speaker-list" font-size="27" font-weight="500" fill="var(--grey-text)" text-anchor="end">
      <text x="1207" y="963">BISHOP DANIEL MAREMBO</text>
      <text x="1207" y="1012">PROPHET THEODORE ALAMBA</text>
      <text x="1207" y="1062">PROPHET EMMANUEL CHEN KOBALI</text>
      <text x="1207" y="1111">PROPHET SAMUEL TENGA</text>
      <text x="1207" y="1160">PROPHET ELIAS MORANO</text>
    </g>
    <g stroke="var(--grey-text)" stroke-width="1" opacity=".6">
      <line x1="1000" y1="974" x2="1207" y2="974"/>
      <line x1="935" y1="1023" x2="1207" y2="1023"/>
      <line x1="900" y1="1073" x2="1207" y2="1073"/>
      <line x1="995" y1="1122" x2="1207" y2="1122"/>
      <line x1="1000" y1="1172" x2="1207" y2="1172"/>
    </g>
  </g>

  <!-- contact -->
  <g class="contact">
    <polygon points="920,1195 1240,1195 1240,1257 980,1257" fill="var(--orange)"/>
    <text class="display" x="1206" y="1243" text-anchor="end" font-size="42" font-weight="500" fill="var(--white)">CONTACT US</text>
    <polygon points="845,1322 895,1262 1240,1262 1240,1322" fill="var(--white)"/>
    <text class="display" x="1207" y="1311" text-anchor="end" font-size="48" font-weight="500" fill="var(--ink)">1 (207) 555 0142</text>
    <text class="body-text" x="1207" y="1357" text-anchor="end" font-size="21" font-weight="600" fill="var(--ink)">contact@cedarhollow.org</text>
    <text class="body-text" x="1207" y="1398" text-anchor="end" font-size="21" font-weight="600" fill="var(--ink)">www.lanternhouse.org</text>
  </g>

  <!-- theme verse -->
  <g class="theme-verse">
    <text class="body-text" x="310" y="950" font-size="46" font-weight="700" fill="var(--white)" letter-spacing="2">YOUR</text>
    <text class="body-text" x="308" y="1028" font-size="86" font-weight="800" fill="var(--white)">SON</text>
    <text class="body-text" transform="translate(508,996) rotate(-90)" text-anchor="middle" font-size="20" font-weight="700" fill="var(--white)">AND</text>
    <rect class="figure-children" role="img" aria-label="Silhouette of two children" x="518" y="962" width="26" height="64" rx="6" fill="var(--white)" opacity=".25"/>
    <text class="body-text" x="312" y="1082" font-size="52" font-weight="700" fill="var(--white)">DAUGHTER</text>
    <text class="body-text" transform="translate(331,1128) rotate(-90)" text-anchor="middle" font-size="20" font-weight="700" fill="var(--white)">SHALL</text>
    <text class="display" x="340" y="1158" font-size="86" font-weight="600" fill="var(--yellow)" textLength="292" lengthAdjust="spacingAndGlyphs">PROPHESY</text>
    <rect class="figure-girl" role="img" aria-label="Silhouette of a young girl" x="636" y="1040" width="38" height="118" rx="10" fill="var(--white)" opacity=".25"/>
  </g>
</svg>
</body>
</html>
```